Brandt WordPress Design Contest

We need a wordpress design that will incorporate a professional color scheme with company logo in a clean layout. The design needs to consider that this will be developed on a responsive theme. Colors are up to the designer - The green of the logo with black, gray or an accent color. Client wants a 'modern' look.

Industry/Entity Type

It Company

Number of Pages Required

1 page

Font styles to use
Serif
Sans Serif

Requirements
Must have
• Navigation: 1) Home 2) All Auctions 3) Real Estate for Sale 4) Services 5) About Us 6) Contact Us
• Colors - a corporate look with professional color scheme. Green of logo + black and gray, or an eggshell/light beige, or any other accent that keeps within a corporate look.
• In header - logo (attached) , and contact info :5127 Old Harrow Lane, Scottsville, KY 42179
• 270-555-3946
• Fax: 270-555-3947
• Email:info@brandtpropertybidhouse.example
• Design will feature a full width (960 px) slideshow - use a stock photo for real estate.
• Widgets in sidebar or where appropriate - 1) Email Signup 2) Message of the Day 3) Upcoming Auctions 4) News&Events blog 5) Testimonials 6) Social media - FB, twitter, youtube, pinterest, google+
• Footer will have company logo, association logos (attached) and contact info, with another widget area if necessary
Nice to have
• use of drop down menu styling - Upcoming Auctions / Online Auctions/ Past Auctions under the "Auction Calendar" menu item

```html
<!DOCTYPE html>
<html lang="en">
<head>
<meta charset="utf-8">
<title>Brandt Real Estate &amp; Auction Co.</title>
<link rel="stylesheet" href="https://fonts.googleapis.com/css2?family=Arimo:wght@400;700&family=Open+Sans:wght@400;600;700&family=Roboto+Condensed:wght@400&display=swap">
<style>
:root{
  --green:#3a7d1e;
  --green-bright:#6cb52d;
  --green-dark:#2e6a17;
  --brand-green:#1f7a3a;
  --navy:#0f2535;
  --footer:#13232f;
  --bar:#3a3a3a;
  --light:#f0f0f0;
  --beige:#e8dfc8;
  --ink:#2b2b2b;
  --muted:#666;
  --rule:#d6d6d6;
  --white:#fff;
}
*{margin:0;padding:0;box-sizing:border-box}
html,body{width:671px;height:1200px;overflow:hidden}
body{position:relative;font-family:"Open Sans",Arial,sans-serif;color:var(--ink);background:var(--white)}
a{text-decoration:none;color:inherit}
.abs{position:absolute}
svg{display:block}

/* header */
.site-header{left:0;top:0;width:671px;height:97px;background:linear-gradient(#fff 40%,#e9e9e9)}
.brand{left:70px;top:28px;display:flex;align-items:center;gap:8px}
.brand-mark{width:26px;height:26px;background:var(--brand-green)}
.brand-name{font-family:"Arimo",Arial,sans-serif;font-weight:700;font-size:34px;color:var(--brand-green);line-height:1}
.social{left:498px;top:0;display:flex;gap:4px}
.social span{width:18px;height:24px;clip-path:polygon(0 0,100% 0,100% 100%,50% 80%,0 100%)}
.contact{font-size:8.5px;color:#333;display:flex;align-items:center;gap:5px;white-space:nowrap}
.contact svg{width:9px;height:9px;fill:#333}

/* nav */
.main-nav{left:0;top:97px;width:671px;height:23px;background:var(--navy)}
.main-nav a{position:absolute;top:0;height:23px;line-height:23px;font-family:"Roboto Condensed",sans-serif;font-size:8px;color:#fff;text-transform:uppercase;white-space:nowrap}
.main-nav a.active{background:var(--green-dark);width:54px;text-align:center}

/* hero */
.hero{left:0;top:120px;width:671px;height:246px;background:linear-gradient(100deg,#5a2a12 0%,#b8732e 30%,#e0a54a 55%,#c9862c 70%,#4b5a3a 100%)}
.hero-caption{left:60px;top:96px;width:302px;height:70px;background:rgba(25,25,25,.72);padding:10px 8px;color:#fff}
.hero-caption h2{font-size:8px;font-weight:600;text-transform:uppercase;margin-bottom:6px;white-space:nowrap}
.hero-caption p{font-size:6.6px;line-height:1.35;text-align:center}
.btn{display:flex;align-items:center;background:var(--green-bright);color:#fff;font-weight:600;text-transform:uppercase;position:absolute;white-space:nowrap}
.btn .label{flex:1;text-align:center}
.btn .go{height:100%;display:flex;align-items:center;justify-content:center;background:var(--green-dark)}
.btn .go svg{fill:#fff}
.hero .btn{left:146px;top:173px;width:117px;height:28px;font-size:9px}
.hero .btn .go{width:30px}

/* welcome */
.welcome{left:0;top:366px;width:671px;height:214px;background:var(--light);text-align:center}
.welcome h1{position:absolute;top:18px;width:100%;font-family:"Arimo",Arial,sans-serif;font-size:15px;color:var(--green);font-weight:700}
.welcome h3{position:absolute;top:37px;width:100%;font-family:"Arimo",Arial,sans-serif;font-size:11px;font-weight:400;color:var(--green)}
.welcome .rule{position:absolute;left:60px;top:53px;width:553px;height:1px;background:var(--rule)}
.welcome .copy{position:absolute;left:75px;top:70px;width:521px;font-size:7.6px;line-height:1.45;color:var(--muted)}
.welcome .copy p{margin-bottom:10px}
.welcome .btn{left:278px;top:175px;width:116px;height:26px;font-size:8.5px}
.welcome .btn .go{width:30px}

/* feature band */
.feature{left:0;top:580px;width:671px;height:204px;background:var(--beige)}
.feature h2{position:absolute;top:20px;font-family:"Arimo",Arial,sans-serif;font-size:14px;font-weight:400;color:#222}
.feature .rule{position:absolute;left:60px;top:44px;width:553px;height:1px;background:#cfc4a8}
.feature .divider{position:absolute;left:383px;top:50px;width:1px;height:132px;background:#cfc4a8}
.motd-photo{left:68px;top:57px;width:154px;height:114px;background:#fff;padding:4px;box-shadow:0 0 2px rgba(0,0,0,.2)}
.motd-photo div{width:100%;height:100%;background:linear-gradient(#3f7fd0,#8cc0ec 55%,#e8e2d6 62%,#c97b5a 85%,#6f8d40)}
.motd-info{left:236px;top:65px;width:115px}
.motd-info h4{font-family:"Arimo",Arial,sans-serif;font-size:8.5px;line-height:1.15;color:#333;text-transform:uppercase}
.motd-info .ago{font-size:6.5px;color:#555;margin-top:9px}
.motd-info .stat{font-family:"Arimo",Arial,sans-serif;font-size:8.5px;font-weight:700;text-transform:uppercase;margin-top:7px}
.motd-info .stat b{color:var(--green)}
.feature .btn.small{height:17px;font-size:6.5px}
.feature .btn.small .go{width:18px}
.news{left:395px;top:57px;width:210px}
.news h5{font-family:"Arimo",Arial,sans-serif;font-size:8.5px;font-weight:400;color:#222}
.news p{font-size:6.5px;line-height:1.35;color:#555;margin-bottom:9px}

/* auctions */
.auctions{left:0;top:784px;width:671px;height:213px;background:var(--light)}
.auctions h2{position:absolute;top:22px;width:100%;text-align:center;font-family:"Arimo",Arial,sans-serif;font-size:14px;color:var(--green)}
.auctions .rule{position:absolute;left:60px;top:47px;width:553px;height:1px;background:var(--rule)}
.card{position:absolute;top:56px;width:126px;height:158px;background:#fff;border:1px solid #dcdcdc;text-align:center}
.card .photo{height:99px}
.card .city{font-size:7.5px;margin-top:10px;color:#333}
.card .ago{font-size:6.5px;color:#555;margin-top:2px}
.card .price{font-size:7.5px;font-weight:700;margin-top:2px}
.arrow{position:absolute;top:108px;width:22px;height:22px;border:1px solid #888;border-radius:50%;display:flex;align-items:center;justify-content:center}
.arrow svg{stroke:#555;fill:none;stroke-width:1.5}

/* mailing */
.mailing{left:0;top:997px;width:671px;height:86px;background:#fff;text-align:center}
.mailing h2{position:absolute;top:26px;width:100%;font-family:"Arimo",Arial,sans-serif;font-size:12px;font-weight:700;color:#333}
.mailing p{position:absolute;top:46px;width:100%;font-size:7px;color:#444}
.mailing .field{left:193px;top:68px;width:198px;height:18px;border:1px solid #ccc;font-size:6px;color:#999;text-align:left;padding:4px 7px;background:#fff}
.mailing .submit{left:395px;top:68px;width:56px;height:18px;background:var(--green-bright);color:#fff;font-size:7px;font-weight:700;line-height:18px}

/* footer */
.site-footer{left:0;top:1090px;width:671px;height:86px;background:var(--footer);color:#fff}
.site-footer h6{position:absolute;top:12px;font-size:6.5px;font-weight:600;text-transform:uppercase}
.site-footer .links{left:71px;top:27px;font-size:6.5px;line-height:11.5px;color:#cfd6dc}
.site-footer .vline{left:178px;top:18px;width:1px;height:50px;background:#2d4050}
.badge{position:absolute;top:27px;height:20px;background:#fff}
.fcontact{font-size:6.5px;color:#cfd6dc;display:flex;align-items:center;gap:5px;white-space:nowrap}
.fcontact svg{width:8px;height:8px;fill:#cfd6dc}
.legal{left:0;top:1176px;width:671px;height:24px;background:var(--bar);color:#ddd;font-size:6px;text-align:center;line-height:24px}
</style>
</head>
<body>

<header class="site-header abs">
  <div class="brand abs"><span class="brand-mark"></span><span class="brand-name">Brandt</span></div>
  <div class="social abs" aria-label="Social media links">
    <span style="background:#3b5998"></span>
    <span style="background:#1da1f2"></span>
    <span style="background:#0e76a8"></span>
    <span style="background:#d34836"></span>
    <span style="background:#c4302b"></span>
  </div>
  <div class="contact abs" style="left:447px;top:63px">
    <svg viewBox="0 0 10 10"><path d="M2 0l2 2-1 1.5c.8 1.5 2 2.7 3.5 3.5L8 6l2 2-1.5 2C4 10 0 6 0 1.5z"/></svg>270-555-3946</div>
  <div class="contact abs" style="left:530px;top:63px">
    <svg viewBox="0 0 10 10"><path d="M2 0h5v3H2zM0 3h10v5H8v2H2V8H0zM3 6v3h4V6z"/></svg>270-555-3946</div>
  <div class="contact abs" style="left:447px;top:78px">
    <svg viewBox="0 0 10 10"><path d="M0 2h10v6H0zm1 1v.5l4 2.5 4-2.5V3L5 5.2z"/></svg>info@brandtpropertybidhouse.example</div>
</header>

<nav class="main-nav abs">
  <a class="active" href="#" style="left:143px">Home</a>
  <a href="#" style="left:208px">All Auctions</a>
  <a href="#" style="left:276px">Real Estate for Sale</a>
  <a href="#" style="left:366px">Services</a>
  <a href="#" style="left:422px">About Us</a>
  <a href="#" style="left:480px">Contact Us</a>
</nav>

<section class="hero abs" role="img" aria-label="Photo of a modern home's open living room and terrace at sunset overlooking the sea">
  <div class="hero-caption abs">
    <h2>Create, complete, send and sign property documents online</h2>
    <p>Create, complete, send and sign property documents online, in a way that is faster and more secure than traditional paper property documents. We streamline your workflow, while keeping the process secure and organised.</p>
  </div>
  <a class="btn" href="#"><span class="label">Read More</span><span class="go"><svg width="10" height="10" viewBox="0 0 10 10"><circle cx="5" cy="5" r="5"/><path d="M4 2.5L6.5 5 4 7.5" stroke="#2e6a17" stroke-width="1.6" fill="none"/></svg></span></a>
</section>

<section class="welcome abs">
  <h1>WELCOME TO BRANDT REAL ESTATE &amp; AUCTION CO.</h1>
  <h3>MAKE YOUR DREAM PROPERTY ONLINE</h3>
  <div class="rule"></div>
  <div class="copy">
    <p>Lorem ipsum dolor sit amet, consectetur adipiscing elit. In eu elementum tortor, at tincidunt quam. Suspendisse tincidunt tellus arcu. Mauris facilisis gravida condimentum. Donec ultrices risus quis volutpat pharetra.</p>
    <p>Ut laoreet diam feugiat, pulvinar nibh sit amet, facilisis urna. Etiam dictum augue neque, non vestibulum magna malesuada id. Nunc vitae tempus tortor, nec condimentum augue. Mauris semper aliquam odio in auctor. Morbi hendrerit et tellus sed fermentum.</p>
    <p>Ut id nisi varius, viverra leo at, sodales ante. Vestibulum mattis tortor in est euismod tristique.</p>
  </div>
  <a class="btn" href="#"><span class="label">Read More</span><span class="go"><svg width="10" height="10" viewBox="0 0 10 10"><circle cx="5" cy="5" r="5"/><path d="M4 2.5L6.5 5 4 7.5" stroke="#2e6a17" stroke-width="1.6" fill="none"/></svg></span></a>
</section>

<section class="feature abs">
  <h2 style="left:65px">MESSAGE OF THE DAY</h2>
  <h2 style="left:397px">NEWS/EVENTS</h2>
  <div class="rule"></div>
  <div class="divider"></div>
  <div class="motd-photo abs"><div role="img" aria-label="Photo of a white stucco villa with a landscaped garden under a blue sky"></div></div>
  <div class="motd-info abs">
    <h4>2BR, Financial District East Virginia, California</h4>
    <p class="ago">about 15 hours on site</p>
    <p class="stat">Price : <b>$5,350</b></p>
    <p class="stat" style="margin-top:4px">Time Left : <b>2 Days</b></p>
  </div>
  <a class="btn small" href="#" style="left:236px;top:172px;width:77px"><span class="label">View Details</span><span class="go"><svg width="8" height="8" viewBox="0 0 10 10"><circle cx="5" cy="5" r="5"/><path d="M4 2.5L6.5 5 4 7.5" stroke="#2e6a17" stroke-width="1.6" fill="none"/></svg></span></a>
  <div class="news abs">
    <h5>Latest News 1</h5>
    <p>Lorem ipsum dolor sit amet, consectetuerdi piscing elit, sed diam nonumm.</p>
    <h5>Coming Events</h5>
    <p>Lorem ipsum dolor sit amet, consectetuerdi piscing elit, sed diam nonumm.</p>
    <h5>Latest News 2</h5>
    <p>Lorem ipsum dolor sit amet, consectetuerdi piscing elit, sed diam nonumm.</p>
  </div>
  <a class="btn small" href="#" style="left:395px;top:172px;width:77px"><span class="label">More News</span><span class="go"><svg width="8" height="8" viewBox="0 0 10 10"><circle cx="5" cy="5" r="5"/><path d="M4 2.5L6.5 5 4 7.5" stroke="#2e6a17" stroke-width="1.6" fill="none"/></svg></span></a>
</section>

<section class="auctions abs">
  <h2>UPCOMING AUCTIONS</h2>
  <div class="rule"></div>
  <div class="arrow" style="left:18px"><svg width="8" height="8" viewBox="0 0 8 8"><path d="M5 1L2 4l3 3"/></svg></div>
  <div class="card" style="left:68px">
    <div class="photo" role="img" aria-label="Photo of a white villa with garden" style="background:linear-gradient(#3f7fd0,#9cc8ee 55%,#e9e4d8 65%,#6f8d40)"></div>
    <p class="city">Atlanta, GA</p><p class="ago">about 12 hours on site</p><p class="price">$2,350</p>
  </div>
  <div class="card" style="left:206px">
    <div class="photo" role="img" aria-label="Photo of a two-storey suburban house with lawn" style="background:linear-gradient(#a9c8e6,#d8cba4 45%,#8a7a5a 65%,#4f7d2e)"></div>
    <p class="city">Atlanta, GA</p><p class="ago">about 12 hours on site</p><p class="price">$2,350</p>
  </div>
  <div class="card" style="left:343px">
    <div class="photo" role="img" aria-label="Photo of a Mediterranean-style home with terracotta roof" style="background:linear-gradient(#b9d3ea,#d9c49a 45%,#b08860 70%,#557a36)"></div>
    <p class="city">Atlanta, GA</p><p class="ago">about 12 hours on site</p><p class="price">$2,350</p>
  </div>
  <div class="card" style="left:480px">
    <div class="photo" role="img" aria-label="Photo of a minimalist white house with glass wall and lawn" style="background:linear-gradient(#e6e6e6,#f4f4f2 45%,#a8633a 55%,#7fb03a)"></div>
    <p class="city">Atlanta, GA</p><p class="ago">about 12 hours on site</p><p class="price">$2,350</p>
  </div>
  <div class="arrow" style="left:630px"><svg width="8" height="8" viewBox="0 0 8 8"><path d="M3 1l3 3-3 3"/></svg></div>
</section>

<section class="mailing abs">
  <h2>JOIN OUR MAILING LIST</h2>
  <p>Enter your email address, choose the types of auctions that interest you and click submit.</p>
  <div class="field abs">Type your email id</div>
  <div class="submit abs">SUBMIT</div>
</section>

<footer class="site-footer abs">
  <h6 style="left:71px">Company Information</h6>
  <div class="links abs">About Us<br>All Auction<br>Contact Us</div>
  <div class="vline abs"></div>
  <h6 style="left:199px">Affiliaites</h6>
  <div class="badge" style="left:201px;width:55px"></div>
  <div class="badge" style="left:266px;width:50px;border-radius:50%"></div>
  <div class="badge" style="left:326px;width:54px"></div>
  <h6 style="left:451px">Contact Info</h6>
  <div class="fcontact abs" style="left:451px;top:28px"><svg viewBox="0 0 10 10"><path d="M5 0a3.5 3.5 0 0 0-3.5 3.5C1.5 6 5 10 5 10s3.5-4 3.5-6.5A3.5 3.5 0 0 0 5 0zm0 5a1.5 1.5 0 1 1 0-3 1.5 1.5 0 0 1 0 3z"/></svg>5127 Old Harrow Lane, Scottsville, KY 42179</div>
  <div class="fcontact abs" style="left:451px;top:43px"><svg viewBox="0 0 10 10"><path d="M2 0l2 2-1 1.5c.8 1.5 2 2.7 3.5 3.5L8 6l2 2-1.5 2C4 10 0 6 0 1.5z"/></svg>270-555-3946</div>
  <div class="fcontact abs" style="left:512px;top:43px"><svg viewBox="0 0 10 10"><path d="M2 0h5v3H2zM0 3h10v5H8v2H2V8H0zM3 6v3h4V6z"/></svg>270-555-3946</div>
  <div class="fcontact abs" style="left:451px;top:58px"><svg viewBox="0 0 10 10"><path d="M0 2h10v6H0zm1 1v.5l4 2.5 4-2.5V3L5 5.2z"/></svg>info@brandtpropertybidhouse.example</div>
</footer>
<div class="legal abs">© 2015, All Rights Reserved, Brandt Real Estate Auction &amp; Co.</div>

</body>
</html>
```